TLMS Coatings Bucket Label 5 Gallon Buckets

We are selling resins "TLMS Coatings". The labels will be for 5 gallon buckets and smaller color packs. We have 9-10 different products. with some variations. We need to disign one label then applly to all. We have some generic labels but need them to be more bold and on brand. Sample of generic attached. Also there will be color codes part A part B for each resin that will be matching colors per resin but different for each product for easy identity.

Both Labels will be Stickers

1 Design front of Bucket with Company Branding
2 Technical Data on of Bucket

Our website is www.tealmooseshopslabs.example for branding

Here are logos that we have on t Shirts.

The shield and TLMS Coatings are needed on each

Colors
EB3D1F
EC4F4E
F09395
F8D3D4
FCEDEE

Requirements
Nice to have
• We would like our logo incorporated into the label but also needs product names and specs

```html
<!DOCTYPE html>
<html lang="en">
<head>
<meta charset="utf-8">
<title>TLMS Coatings 650 Polyaspartic Resin Label</title>
<link href="https://fonts.googleapis.com/css2?family=Exo+2:wght@700;800&family=Russo+One&display=swap" rel="stylesheet">
<style>
  :root {
    --page-bg: #f6f6f8;
    --label-black: #0a0a0b;
    --label-charcoal: #3a3a3d;
    --label-grey: #6c6c70;
    --brand-red: #d3141a;
    --brand-red-light: #ec4f4e;
    --brand-red-soft: #f09395;
    --ink-white: #f2f2f2;
    --badge-white: #ffffff;
  }
  * { margin: 0; padding: 0; box-sizing: border-box; }
  html, body {
    width: 1200px;
    height: 1200px;
    overflow: hidden;
    background: var(--page-bg);
  }
  .canvas {
    position: relative;
    width: 1200px;
    height: 1200px;
  }
  .label {
    position: absolute;
    left: 150px;
    top: 240px;
    width: 900px;
    height: 720px;
    overflow: hidden;
    background: var(--label-black);
  }
  .label__pattern {
    position: absolute;
    inset: 0;
    background:
      linear-gradient(115deg, transparent 0 8%, rgba(211,20,26,0.55) 8% 12%, transparent 12% 100%),
      linear-gradient(90deg, var(--label-grey) 0%, var(--label-charcoal) 12%, var(--label-black) 30%, var(--label-black) 70%, var(--label-charcoal) 86%, var(--label-grey) 100%);
  }
  .brand-mark {
    position: absolute;
    left: 325px;
    top: 42px;
    width: 250px;
    height: 250px;
    border-radius: 50%;
    background: var(--label-black);
    border: 10px solid var(--brand-red);
  }
  .brand-name {
    position: absolute;
    left: 0;
    right: 0;
    top: 310px;
    text-align: center;
    font-family: "Exo 2", sans-serif;
    font-weight: 800;
    font-size: 104px;
    line-height: 1;
    color: var(--brand-red);
    letter-spacing: 2px;
  }
  .product-code {
    position: absolute;
    left: 256px;
    top: 428px;
    width: 388px;
    height: 122px;
    background: var(--brand-red);
    border-radius: 10px 10px 0 0;
    text-align: center;
    font-family: "Russo One", sans-serif;
    font-size: 112px;
    line-height: 124px;
    color: var(--ink-white);
    letter-spacing: 6px;
  }
  .product-band {
    position: absolute;
    left: 0;
    right: 0;
    top: 546px;
    height: 116px;
    background: linear-gradient(90deg, var(--brand-red-light) 0%, var(--brand-red) 25%, var(--brand-red) 75%, var(--brand-red-light) 100%);
    display: flex;
    flex-direction: column;
    align-items: center;
    justify-content: center;
    font-family: "Exo 2", sans-serif;
    font-weight: 800;
    font-size: 42px;
    line-height: 1.1;
    color: var(--ink-white);
    letter-spacing: 1px;
  }
  .volume {
    position: absolute;
    left: 0;
    right: 0;
    top: 672px;
    text-align: center;
    font-family: "Exo 2", sans-serif;
    font-weight: 700;
    font-size: 28px;
    line-height: 1;
    color: var(--ink-white);
    letter-spacing: 2px;
  }
  .part-badge {
    position: absolute;
    left: 712px;
    top: 414px;
    width: 96px;
    height: 96px;
    border-radius: 50%;
    background: var(--badge-white);
    border: 4px solid var(--badge-white);
    box-shadow: inset 0 0 0 3px var(--label-grey);
    display: flex;
    flex-direction: column;
    align-items: center;
    justify-content: center;
    font-family: "Exo 2", sans-serif;
    font-weight: 800;
    font-size: 19px;
    line-height: 1.1;
    color: var(--brand-red-soft);
  }
</style>
</head>
<body>
  <main class="canvas">
    <section class="label">
      <div class="label__pattern" role="img" aria-label="Sweeping diagonal pinstripe pattern in grey and red across a black background"></div>
      <div class="brand-mark" role="img" aria-label="Company shield mark"></div>
      <div class="brand-name">TLMS</div>
      <div class="product-code">650</div>
      <div class="product-band">
        <span>POLYASPARTIC</span>
        <span>RESIN</span>
      </div>
      <div class="part-badge">
        <span>PART A</span>
        <span>(1:1)</span>
      </div>
      <div class="volume">5 GALLON</div>
    </section>
  </main>
</body>
</html>
```